Business card and A5 "with our compliments" note
Quellwick - a service design company
I need double sided standard sized Business Card [3.5" x 2"]
Use whatever works
Bright & Fun-filled
Tobin Vrask
Director
14 Korimu Lane
Hollow Bay
Auckland 1187
NEW ZEALAND
tobin@quellwick.example.nz
www.quellwick.example.nz
The business card should surprise: at first glance it should resemble something else. My business is about inquiry, research, and design e.g. a sticky note with ideas on it e.g. part of a questionnaire e.g. a card from a popular game like the "chance" card in Tradeworld e.g. a jigsaw piece
Graphical rending as per comments OR expanded logo OR ....
Designers can remove the tagline if convenient, but the business card should then also say "service and programme design" somewhere

```html
<!DOCTYPE html>
<html lang="en">
<head>
<meta charset="utf-8">
<title>Quellwick business card</title>
<link href="https://fonts.googleapis.com/css2?family=Arimo:wght@400;700&display=swap" rel="stylesheet">
<style>
  :root {
    --backdrop: #d8d9da;
    --card-white: #ffffff;
    --band: #2fa044;
    --band-edge: #1f7a31;
    --accent: #ffd23a;
    --ink: #1b1b1b;
    --ink-soft: #3a3a3a;
    --rule: #e4efe6;
    --on-band: #ffffff;
  }
  * { margin: 0; padding: 0; box-sizing: border-box; }
  html, body { width: 1200px; height: 850px; overflow: hidden; }
  body {
    background: var(--backdrop);
    font-family: "Arimo", Arial, sans-serif;
    position: relative;
  }
  .card {
    position: absolute;
    width: 540px;
    height: 309px;
    border-radius: 22px;
    overflow: hidden;
    display: flex;
    background: var(--card-white);
    box-shadow: 0 10px 24px rgba(0,0,0,0.25);
  }
  /* ruled lines, like a questionnaire sheet */
  .ruled {
    background-image: repeating-linear-gradient(
      to bottom, transparent 0 33px, var(--rule) 33px 35px);
  }
  /* jigsaw tab joining band and face */
  .puzzle-tab {
    position: absolute;
    width: 44px; height: 44px;
    border-radius: 50%;
    background: var(--band);
    border: 5px solid var(--band-edge);
  }
  /* Front */
  .card--front { left: 90px; top: 110px; }
  .front__face {
    flex: 0 0 340px;
    display: flex;
    align-items: center;
    justify-content: center;
  }
  .front__band {
    flex: 1;
    background: var(--band);
    border-left: 5px solid var(--band-edge);
    display: flex;
    align-items: center;
    justify-content: center;
  }
  .card--front .puzzle-tab { left: 318px; top: 232px; }
  .front__service {
    writing-mode: vertical-rl;
    color: var(--on-band);
    font-size: 17px;
    font-weight: 700;
    letter-spacing: 0.5px;
  }
  .wordmark {
    display: flex;
    align-items: center;
    gap: 12px;
  }
  .wordmark__dot {
    width: 50px; height: 50px;
    border-radius: 50%;
    background: var(--accent);
    flex: none;
  }
  .wordmark__name {
    font-weight: 700;
    font-size: 44px;
    letter-spacing: -1px;
    color: var(--ink);
  }
  /* Back */
  .card--back { left: 570px; top: 430px; }
  .back__band {
    flex: 0 0 150px;
    background: var(--band);
    border-right: 5px solid var(--band-edge);
    position: relative;
  }
  .card--back .puzzle-tab { left: 128px; top: 252px; }
  .back__band .wordmark {
    position: absolute;
    left: 50%; top: 50%;
    transform: translate(-50%, -50%) rotate(-90deg);
  }
  .back__band .wordmark__name { color: var(--on-band); font-size: 38px; }
  .back__band .wordmark__dot { width: 40px; height: 40px; }
  .back__details {
    flex: 1;
    padding: 40px 0 0 34px;
    color: var(--ink);
  }
  .person__name {
    display: inline-block;
    font-size: 24px;
    font-weight: 700;
    letter-spacing: 1.5px;
    background: linear-gradient(transparent 60%, var(--accent) 60%);
  }
  .person__role { font-size: 17px; margin-top: 4px; letter-spacing: 0.5px; }
  .address, .contact {
    font-size: 12.5px;
    line-height: 17px;
    color: var(--ink-soft);
    list-style: none;
  }
  .address { margin-top: 18px; }
  .contact { margin-top: 10px; }
  .contact li { display: flex; align-items: center; gap: 6px; }
  .tick-box { width: 12px; height: 12px; flex: none; }
</style>
</head>
<body>
  <section class="card card--front" aria-label="Business card front">
    <div class="front__face ruled">
      <div class="wordmark">
        <span class="wordmark__dot"></span>
        <span class="wordmark__name">Quellwick</span>
      </div>
    </div>
    <div class="front__band">
      <p class="front__service">Service and Programme Design</p>
    </div>
    <span class="puzzle-tab"></span>
  </section>

  <section class="card card--back" aria-label="Business card back">
    <div class="back__band">
      <div class="wordmark">
        <span class="wordmark__dot"></span>
        <span class="wordmark__name">Quellwick</span>
      </div>
    </div>
    <span class="puzzle-tab"></span>
    <div class="back__details ruled">
      <h1 class="person__name">Tobin Vrask</h1>
      <p class="person__role">Director</p>
      <ul class="address">
        <li>14 Korimu Lane</li>
        <li>Hollow Bay Auckland</li>
        <li>1187 , NEW ZEALAND</li>
      </ul>
      <ul class="contact">
        <li><svg class="tick-box" viewBox="0 0 12 12"><rect x="0.5" y="0.5" width="11" height="11" fill="none" stroke="#1f7a31"/><path d="M2.5 6.2 5 8.5 9.5 3.5" fill="none" stroke="#2fa044" stroke-width="1.8"/></svg>C : +64 21 555 0192</li>
        <li><svg class="tick-box" viewBox="0 0 12 12"><rect x="0.5" y="0.5" width="11" height="11" fill="none" stroke="#1f7a31"/><path d="M2.5 6.2 5 8.5 9.5 3.5" fill="none" stroke="#2fa044" stroke-width="1.8"/></svg>E : tobin@quellwick.example.nz</li>
        <li><svg class="tick-box" viewBox="0 0 12 12"><rect x="0.5" y="0.5" width="11" height="11" fill="none" stroke="#1f7a31"/><path d="M2.5 6.2 5 8.5 9.5 3.5" fill="none" stroke="#2fa044" stroke-width="1.8"/></svg>w : www.quellwick.example.nz</li>
      </ul>
    </div>
  </section>
</body>
</html>
```